Lydia Vandermere personal business/name cards and stationery brief

I am looking for a simple design on my personal business cards, that I may use for all my stationery. All my stationery would be cream or ivory textured card, or cream/ivory quality paper. I am director of my family company and also property developer. But am wishing to have basic business cards that I can use across both businesses. I do not wish to have a title, just my initials as a focal point.
Target Market(s)
These are my personal business cards and stationery. I am looking for an elegant, relatively understated design that exudes wealth. There is no target audience, other than clients or people I already do business with. However design must be stylish and timeless.
If I am handing out my business card to anyone I do not do business with, or they are not contracting to me or my company currently, then i would like the target audience to wish they were.
I am 54 yeas of age, and my business cards must denote respect and class.
Industry/Entity Type
Business
Contact Information for Business Card
LV
Lydia Vandermere
Justice of the Peace
Possible rear of card
Mobile number
Email
Font styles to use
Requirements
Must have
- LV to be somehow entwined as a logo on the front of the card above my name
- These cards must state that I am a Justice of the Peace
- Colours only ivory or cream card with texture, and gold elegant font.
- Must be able to be used on all my stationery products
- Must be elegant, timeless and not cluttered
- Below are just some design I like. There is something in each design I like.
Nice to have
- I would like my initials to be the centre piece of the card. Somehow entwined together elegantly in a logo of sorts that I can use across all my stationery. But if not my initials, then something that is different and stands out from the rest.
Should not have
- Not gawdy or young. No colour. Nothing outlandish.

```html
<!DOCTYPE html>
<html lang="en">
<head>
<meta charset="utf-8">
<title>Lydia Vandermere – Business Card</title>
<link href="https://fonts.googleapis.com/css2?family=Cinzel:wght@500&family=Quattrocento:wght@400&family=Roboto:wght@400&display=swap" rel="stylesheet">
<style>
  :root {
    --backdrop: #72706d;
    --ivory: #fefee8;
    --gold-deep: #a8841f;
    --gold-mid: #d4ad3e;
    --gold-light: #f1df86;
    --gold-ink: #c9a43a;
    --gold-faint: rgba(226, 200, 120, 0.28);
    --ink: #2f302c;
  }
  * { margin: 0; padding: 0; box-sizing: border-box; }
  html, body {
    width: 1200px;
    height: 484px;
    overflow: hidden;
    background: var(--backdrop);
  }
  .canvas {
    position: relative;
    width: 1200px;
    height: 484px;
  }
  .card {
    position: absolute;
    top: 106px;
    width: 452px;
    height: 273px;
    padding: 9px;
    background:
      linear-gradient(180deg, var(--gold-light) 0%, var(--gold-mid) 8%, var(--gold-mid) 88%, var(--gold-deep) 100%),
      var(--gold-mid);
  }
  .card--front { left: 137px; }
  .card--back { left: 610px; }
  .card__face {
    position: relative;
    width: 100%;
    height: 100%;
    background: var(--ivory);
    overflow: hidden;
  }
  .monogram {
    position: absolute;
    left: 0;
    right: 0;
    text-align: center;
    font-family: "Cinzel", serif;
    font-weight: 500;
    letter-spacing: 4px;
    line-height: 1;
  }
  .monogram--front {
    top: 72px;
    font-size: 104px;
    color: var(--gold-ink);
  }
  .monogram--watermark {
    top: 58px;
    font-size: 120px;
    color: var(--gold-faint);
  }
  .details {
    position: absolute;
    left: 0;
    right: 0;
    text-align: center;
    color: var(--ink);
  }
  .details__name {
    top: 86px;
    font-family: "Cinzel", serif;
    font-weight: 500;
    font-size: 21px;
    letter-spacing: 1px;
  }
  .details__role {
    top: 119px;
    font-family: "Roboto", sans-serif;
    font-size: 10.5px;
  }
  .details__phone {
    top: 150px;
    font-family: "Quattrocento", serif;
    font-size: 11px;
  }
  .details__email {
    top: 166px;
    font-family: "Quattrocento", serif;
    font-size: 11px;
  }
</style>
</head>
<body>
  <main class="canvas">
    <section class="card card--front" aria-label="Card front">
      <div class="card__face">
        <div class="monogram monogram--front">LV</div>
      </div>
    </section>

    <section class="card card--back" aria-label="Card back">
      <div class="card__face">
        <div class="monogram monogram--watermark" aria-hidden="true">LV</div>
        <h1 class="details details__name">LYDIA VANDERMERE</h1>
        <p class="details details__role">Justice of the Peace</p>
        <p class="details details__phone">04-218-7731</p>
        <p class="details details__email">lydia@vandermereholdings.com</p>
      </div>
    </section>
  </main>
</body>
</html>
```